Business Card Design for a Sound engineer and DJ

We would like a residn of the business card.

Logo must remain the same.
The card is for the owner of the company.
The business card is in Arabic as the company is based in Kuwait.
The company specializes in sound engineering for singers concerts and events and in addition DJ.
The color options is up to the designer but we would like it masculine as the owner is a man.

Target Market(s)

All ages

Industry/Entity Type

Media

Contact Information for Business Card

Name:
Eng. Tarek Halabi
م/طارق حلبي

The name above is in Arabic and English.

Title: General Manager
Mobile: +965 66307852
Office: +965 22486037
Email: info@sawtarin.net

Address:
Office no. 3
1st floor
Almarfa Complex
Rashed AlQeblawi St.
Salmiya
Kuwait

Instagram: @sawtarin
Snap: sawtarin

Requirements
Nice to have
• can we have Instagram icon and snap icon and a phone vector and email?
• Instead of writing the words

```html
<!DOCTYPE html>
<html lang="en">
<head>
<meta charset="utf-8">
<title>Sawtarin – Business Card</title>
<link href="https://fonts.googleapis.com/css2?family=Open+Sans:wght@400;600;700&family=Cairo:wght@400;600&display=swap" rel="stylesheet">
<style>
  :root {
    --page: #ffffff;
    --card: #0b0c0e;
    --ink: #ffffff;
    --brand: #8a4f9e;
    --accent: #6c7fc0;
    --rule: #d9d9d9;
  }
  html, body {
    margin: 0;
    width: 1200px;
    height: 706px;
    overflow: hidden;
    background: var(--page);
  }
  .card {
    position: relative;
    width: 1200px;
    height: 706px;
    background: var(--card);
    border-radius: 40px;
    overflow: hidden;
    color: var(--ink);
    font-family: "Open Sans", sans-serif;
  }
  .brand {
    position: absolute;
    left: 400px;
    top: 150px;
    width: 340px;
    text-align: center;
  }
  .brand-name {
    margin: 0;
    font-family: "Open Sans", sans-serif;
    font-weight: 700;
    font-size: 60px;
    letter-spacing: 6px;
    color: var(--brand);
    line-height: 1;
    text-transform: uppercase;
  }
  .brand-mark {
    display: block;
    width: 14px;
    height: 14px;
    margin: 0 auto 22px;
    background: var(--brand);
  }
  .brand-tagline {
    margin: 26px 0 0;
    font-weight: 700;
    font-size: 18px;
    letter-spacing: 2.5px;
    color: var(--brand);
    line-height: 1;
  }
  .brand-tagline-ar {
    margin: 8px 0 0;
    font-family: "Cairo", sans-serif;
    font-size: 21px;
    color: var(--brand);
    line-height: 1.2;
  }
  .owner {
    position: absolute;
    left: 40px;
    top: 500px;
    width: 280px;
    text-align: center;
  }
  .owner-name-ar {
    margin: 0;
    font-family: "Cairo", sans-serif;
    font-size: 40px;
    font-weight: 400;
    line-height: 1.15;
  }
  .owner-name {
    margin: 6px 0 0;
    font-weight: 700;
    font-size: 38px;
    line-height: 1.1;
    padding-bottom: 6px;
    border-bottom: 2px solid var(--rule);
  }
  .owner-title {
    margin: 6px 0 0;
    font-weight: 700;
    font-size: 33px;
    color: var(--accent);
    line-height: 1.1;
    letter-spacing: -0.3px;
  }
  .contact {
    position: absolute;
    left: 364px;
    top: 514px;
    margin: 0;
    padding: 0;
    list-style: none;
  }
  .contact li {
    display: flex;
    align-items: center;
    height: 54px;
    font-size: 34px;
    letter-spacing: 0.5px;
  }
  .contact svg {
    width: 36px;
    height: 36px;
    margin-right: 16px;
    flex: none;
  }
  .address {
    position: absolute;
    left: 690px;
    top: 514px;
    display: flex;
  }
  .address svg {
    width: 24px;
    height: 34px;
    margin: 6px 28px 0 0;
    flex: none;
  }
  .address-lines {
    margin: 0;
    font-style: normal;
    font-size: 32px;
    line-height: 37px;
  }
</style>
</head>
<body>
  <div class="card">
    <header class="brand">
      <span class="brand-mark"></span>
      <h1 class="brand-name">Sawtarin</h1>
      <p class="brand-tagline">DJ - SOUND ENG. - LIGHTING</p>
      <p class="brand-tagline-ar" dir="rtl">دي جي - هندسة صوت - إضاءة</p>
    </header>

    <section class="owner">
      <p class="owner-name-ar" dir="rtl">م/طارق حلبي</p>
      <h2 class="owner-name">Tarek Halabi</h2>
      <p class="owner-title">General Manager</p>
    </section>

    <ul class="contact">
      <li>
        <svg viewBox="0 0 36 36" aria-hidden="true">
          <rect x="9" y="2" width="18" height="32" rx="3" fill="none" stroke="var(--accent)" stroke-width="2.5"/>
          <line x1="15" y1="29" x2="21" y2="29" stroke="var(--accent)" stroke-width="2"/>
        </svg>
        +965 66307852
      </li>
      <li>
        <svg viewBox="0 0 36 36" aria-hidden="true">
          <path d="M8 4 L13 4 L16 12 L12 15 C14 20 17 23 22 25 L25 21 L33 24 L33 29 C33 31 31 33 28 32 C17 30 7 20 5 9 C4 6 6 4 8 4 Z" fill="var(--accent)"/>
        </svg>
        +965 22486037
      </li>
      <li>
        <svg viewBox="0 0 36 36" aria-hidden="true">
          <rect x="3" y="8" width="30" height="21" fill="none" stroke="var(--accent)" stroke-width="2.2"/>
          <path d="M3 8 L18 21 L33 8 M3 29 L14 18 M33 29 L22 18" fill="none" stroke="var(--accent)" stroke-width="2.2"/>
        </svg>
        info@sawtarin.net
      </li>
    </ul>

    <div class="address">
      <svg viewBox="0 0 24 34" aria-hidden="true">
        <path d="M12 1 C5.5 1 1 6 1 12 C1 20 12 33 12 33 C12 33 23 20 23 12 C23 6 18.5 1 12 1 Z" fill="var(--accent)"/>
        <circle cx="12" cy="12" r="4" fill="var(--card)"/>
      </svg>
      <address class="address-lines">
        Office no. 3<br>
        1st floor, Almarfa Complex<br>
        Rashed AlQeblawi St.,<br>
        Salmiya, Kuwait.
      </address>
    </div>
  </div>
</body>
</html>
```